Business Card Design for Lawn Management

Lawn Management

Industry/Entity Type

Business

Contact Information for Business Card

Calloway Lawn Management
Joel Calloway
Calloway_Lawn@brindlemail.com
404-555-0172

```html
<!DOCTYPE html>
<html lang="en">
<head>
<meta charset="utf-8">
<title>Calloway Lawn Management — Business Card</title>
<link rel="stylesheet" href="https://fonts.googleapis.com/css2?family=Quicksand:wght@400;600;700&display=swap">
<style>
  :root {
    --page: #e4e4e2;
    --card-black: #0b0b0b;
    --card-edge: #1c1c1c;
    --leaf-green: #3fc12c;
    --text-green: #35b526;
    --grass-dark: #2f5a1c;
    --grass-light: #4f8a2a;
  }
  * { margin: 0; padding: 0; box-sizing: border-box; }
  html, body {
    width: 1200px; height: 894px; overflow: hidden;
    background: var(--page);
    font-family: "Quicksand", sans-serif;
  }
  .sheet {
    width: 1200px; height: 894px;
    display: flex; flex-direction: column; align-items: center; justify-content: center;
    gap: 40px;
  }
  .card {
    position: relative;
    width: 660px; height: 377px;
    border-radius: 30px;
    background: linear-gradient(160deg, var(--card-edge) 0%, var(--card-black) 45%, var(--card-black) 100%);
    overflow: hidden;
    box-shadow: 0 6px 18px rgba(0,0,0,.18);
  }
  /* Front */
  .card-front {
    display: flex; flex-direction: column; align-items: center; justify-content: center; gap: 22px;
  }
  .brand-mark {
    width: 110px; height: 110px; border-radius: 50%;
    background: var(--leaf-green);
  }
  .brand-name {
    color: var(--leaf-green);
    font-weight: 700; font-size: 44px; letter-spacing: 1px;
    text-align: center; line-height: 1.1;
  }
  /* Back */
  .grass-band {
    position: absolute;
    background: linear-gradient(180deg, var(--grass-light), var(--grass-dark));
  }
  .grass-top {
    top: 0; left: 0; width: 100%; height: 34px;
    clip-path: polygon(0 0, 100% 0, 100% 100%, 33% 100%, 28% 0, 0 0, 0 0);
    clip-path: polygon(0 0, 100% 0, 100% 26%, 30% 26%, 27% 100%, 0 100%);
  }
  .grass-left {
    top: 0; left: 0; width: 16px; height: 150px;
  }
  .grass-right {
    right: 0; top: 200px; width: 200px; height: 30px;
    clip-path: polygon(0 0, 100% 0, 100% 100%, 8% 100%);
  }
  .back-brand {
    position: absolute; top: 44px; right: 40px;
    display: flex; align-items: center; gap: 10px;
    color: var(--text-green); font-weight: 700; font-size: 18px;
  }
  .back-brand .dot {
    width: 22px; height: 22px; border-radius: 50%; background: var(--leaf-green);
  }
  .holder-name {
    position: absolute; top: 92px; left: 60px;
    color: var(--text-green); font-weight: 400; font-size: 38px; letter-spacing: 1px;
  }
  .name-rule {
    position: absolute; top: 148px; left: 16px; width: 330px; height: 2px;
    background: var(--text-green);
  }
  .contact {
    position: absolute; top: 176px; left: 110px;
    list-style: none;
    color: var(--text-green); font-size: 20px; line-height: 1.55;
  }
</style>
</head>
<body>
  <main class="sheet">
    <section class="card card-front" aria-label="Business card front">
      <span class="brand-mark" aria-hidden="true"></span>
      <h1 class="brand-name">Calloway Lawn Management</h1>
    </section>

    <section class="card card-back" aria-label="Business card back">
      <div class="grass-band grass-top" role="img" aria-label="Green grass texture band"></div>
      <div class="grass-band grass-left" role="img" aria-label="Green grass texture edge"></div>
      <div class="grass-band grass-right" role="img" aria-label="Green grass texture band"></div>
      <div class="back-brand"><span class="dot" aria-hidden="true"></span>Calloway Lawn Management</div>
      <h2 class="holder-name">Joel Calloway</h2>
      <div class="name-rule"></div>
      <ul class="contact">
        <li>Calloway_Lawn@brindlemail.com</li>
        <li>404-555-0172</li>
      </ul>
    </section>
  </main>
</body>
</html>
```